HIGH-END ANTI AGING START-UP NEEDS DOCUMENT/LETTERHEAD DESIGN!!!!

We are a high end anti-aging and health start-up catering to clients in Stamford and NYC. We just did a logo redesign and are now looking for a letter head design that we can use IN GOOGLE DOCS for marwickcaregroup.example clients. We are REALLY EXCITED to see what you can show us!!!!!!!! We need something sophisticated and MODERN! Thanks so much!

Target Market(s)

High end, boutique medical clients. Our clientele is fairly high profile and we need a sleek, sophisticated letter head to put on all of our marketing materials and medical forms as well.

Industry/Entity Type

Medical

Font styles to use
Serif
Sans Serif

Colors
0255a3
ffffff
00a990
1b1b1b
919191

Requirements
Must have
• Must have the logo and "Marwick Care Group" written somewhere. Must have our URL www.marwickcaregroup.example.
Nice to have
• office phone number (203) 555-0147
Should not have
• Colors outside of our logo colors + grey + black

```html
<!DOCTYPE html>
<html lang="en">
<head>
<meta charset="utf-8">
<title>Marwick Care Group Letterhead</title>
<link href="https://fonts.googleapis.com/css2?family=Lato:wght@300;400;700&family=Noto+Sans:wght@400&display=swap" rel="stylesheet">
<style>
  :root{
    --backdrop:#00a651;
    --paper:#ffffff;
    --brand-green:#1a9a48;
    --brand-blue:#4d7fe0;
    --ink:#1b1b1b;
    --body-grey:#6f6f6f;
  }
  *{margin:0;padding:0;box-sizing:border-box}
  html,body{width:1200px;height:1200px;overflow:hidden}
  body{background:var(--backdrop);font-family:"Lato",sans-serif;position:relative}
  .letterhead{position:absolute;left:190px;top:42px;width:820px;height:1116px;background:var(--paper)}
  .brand{position:absolute;top:100px;left:0;width:100%;text-align:center}
  .brand-dot{display:block;margin:0 auto 18px;width:64px;height:64px;border-radius:50%;background:var(--brand-green)}
  .brand-name{font-weight:700;font-size:24px;letter-spacing:.5px;color:var(--brand-blue)}
  .recipient{position:absolute;top:282px;left:102px;font-family:"Noto Sans",sans-serif;font-size:13.5px;color:var(--ink);line-height:23px;letter-spacing:.5px}
  .meta{position:absolute;top:284px;right:102px;font-size:13.5px;color:var(--ink);line-height:18px}
  .body{position:absolute;top:350px;left:102px;width:616px;font-weight:300;font-size:14.6px;line-height:20.4px;color:var(--body-grey);text-align:justify}
  .body p{margin-bottom:20px}
  .signoff{position:absolute;top:812px;left:102px;color:var(--body-grey)}
  .signoff .regards{font-size:13px;font-weight:300;margin-bottom:14px}
  .signoff .name{font-size:12.5px;color:var(--ink);letter-spacing:.5px}
  .signoff .title{font-size:10.5px;color:var(--ink);letter-spacing:.6px;margin-top:2px}
  .footer-rule{position:absolute;top:946px;height:1px;background:var(--brand-blue)}
  .footer-rule.left{left:102px;width:261px}
  .footer-rule.right{left:454px;width:264px}
  .footer-dot{position:absolute;top:920px;left:382px;width:54px;height:54px;border-radius:50%;background:var(--brand-green)}
  .contact{position:absolute;top:990px;left:0;width:100%;text-align:center;font-size:12.5px;color:var(--ink);white-space:nowrap}
  .contact span{display:inline-flex;align-items:center;gap:8px;vertical-align:middle}
  .contact .sep{color:var(--brand-blue);margin:0 6px}
  .contact .web{font-weight:700}
  .contact svg{width:11px;height:11px;fill:var(--brand-blue)}
  .address{position:absolute;top:1026px;left:0;width:100%;text-align:center;font-size:12.5px;color:var(--ink)}
</style>
</head>
<body>
<main class="letterhead">
  <header class="brand">
    <span class="brand-dot"></span>
    <div class="brand-name">Marwick Care Group</div>
  </header>

  <div class="recipient">
    <div>Dear, Elena Varga</div>
    <div>Creative Director</div>
  </div>
  <div class="meta">
    <div class="date">Date: 12.05.2017</div>
    <div>Halden Point</div>
  </div>

  <section class="body">
    <p>Lorem ipsum dolor sit amet, consectetuer adipiscing elit, sed diam nonummy nibh euismod tincidunt ut laoreet dolore magna aliquam erat volutpat. Ut wisi enim ad minim veniam, quis nostrud exerci tation ullamcorper suscipit lobortis nisl ut aliquip ex ea commodo consequat. Duis autem vel eum iriure dolor in hendrerit in vulputate velit esse molestie consequat, vel illum dolore eu feugiat nulla facilisis at vero eros et accumsan et iusto odio dignissim qui blandit praesent luptatum zzril delenit augue duis dolore te feugait nulla facilisi.</p>
    <p>Lorem ipsum dolor sit amet, cons ectetuer adipiscing elit, sed diam nonummy nibh euismod tincidunt ut laoreet dolore magna aliquam erat volutpat. Ut wisi enim ad minim veniam, quis nostrud exerci tation ullamcorper suscipit lobortis nisl ut aliquip ex ea commodo consequat. Lorem ipsum dolor sit amet, consectetuer adipiscing elit, sed diam nonummy nibh euismod tincidunt ut laoreet dolore magna aliquam erat volutpat. Ut wisi enim ad minim veniam, quis nostrud exerci tation ullamcorper suscipit lobortis.</p>
    <p>nisl ut aliquip ex ea commodo consequat. Duis autem vel eum iriure dolor in hendrerit in vulputate velit esse molestie consequat, vel illum dolore eu feugiat nulla facilisis at vero eros et accumsan et iusto odio dignissim qui blandit praesent luptatum zzril delenit augue duis dolore te feugait nulla facilisi.</p>
    <p>tincidunt ut laoreet dolore magna aliquam erat volutpat. Ut wisi enim ad minim veniam, quis nostrud exerci tation ullamcorper suscipit lobortis nisl ut aliquip ex ea commodo consequat.</p>
  </section>

  <div class="signoff">
    <div class="regards">Regards,</div>
    <div class="name">Daniel Reeve</div>
    <div class="title">EXECUTIVE DIRECTOR</div>
  </div>

  <footer>
    <div class="footer-rule left"></div>
    <span class="footer-dot"></span>
    <div class="footer-rule right"></div>
    <div class="contact">
      <span><svg viewBox="0 0 24 24"><path d="M6.6 10.8a15.1 15.1 0 0 0 6.6 6.6l2.2-2.2c.3-.3.7-.4 1-.2 1.1.4 2.3.6 3.6.6.6 0 1 .4 1 1V20c0 .6-.4 1-1 1A17 17 0 0 1 3 4c0-.6.4-1 1-1h3.5c.6 0 1 .4 1 1 0 1.3.2 2.5.6 3.6.1.3 0 .7-.2 1z"/></svg>(203) 555-0147</span><span class="sep">|</span><span><svg viewBox="0 0 24 24"><path d="M2 5h20v14H2zm2 2v.5l8 5 8-5V7zm0 2.8V17h16V9.8l-8 5z"/></svg>info@marwickcaregroup.example</span><span class="sep">|</span><span class="web"><svg viewBox="0 0 24 24"><path d="M12 2a10 10 0 1 0 0 20 10 10 0 0 0 0-20zm0 3a7 7 0 0 1 0 14 7 7 0 0 1 0-14z"/></svg>www.marwickcaregroup.example</span>
    </div>
    <div class="address">Marwick Care Group, 112 Harbor Ave. Suite 300, Halden Point, 00412</div>
  </footer>
</main>
</body>
</html>
```